Veltrano - Mechanic/Collision Center Business Card

We're looking for a business card design for our mechanic/ collision repair shop.

Can be with colours or monochromatic.

See the attached files.

Many thanks

```html
<!DOCTYPE html>
<html lang="en">
<head>
<meta charset="UTF-8">
<title>Veltrano – Business Card</title>
<link rel="stylesheet" href="https://fonts.googleapis.com/css2?family=Audiowide&family=Montserrat:wght@400;500&display=swap">
<style>
  :root {
    --backdrop: #3b3c3e;
    --card-white: #fbfbfb;
    --card-black: #1c1d1f;
    --brand-blue: #2f7fc1;
    --art-blue: #4ba3d9;
    --art-grey: #8d8f92;
    --text-grey: #5a5c5f;
    --icon-blue: #2c78b8;
    --white: #ffffff;
  }
  * { margin: 0; padding: 0; box-sizing: border-box; }
  html, body { width: 1200px; height: 900px; overflow: hidden; }
  body { background: var(--backdrop); position: relative; font-family: "Montserrat", sans-serif; }

  .card {
    position: absolute;
    width: 700px;
    height: 400px;
    left: 250px;
    box-shadow: 0 10px 30px rgba(0,0,0,0.35);
    overflow: hidden;
  }
  .card--front { top: 40px; background: var(--card-white); }
  .card--back { top: 470px; background: var(--card-black); }

  .company-name {
    position: absolute; left: 58px; top: 78px;
    font-family: "Audiowide", sans-serif;
    font-size: 27px; letter-spacing: 2px;
    color: var(--brand-blue);
  }
  .address {
    position: absolute; left: 62px; top: 128px;
    font-size: 17px; line-height: 25px; color: var(--text-grey);
  }
  .illustration {
    position: absolute; left: 0; bottom: 0;
    width: 370px; height: 190px;
    background: linear-gradient(90deg, var(--art-blue) 0%, var(--art-blue) 55%, var(--art-grey) 100%);
    border-top-right-radius: 60px;
  }
  .contact-list {
    position: absolute; left: 398px; top: 246px;
    list-style: none;
  }
  .contact-list li {
    display: flex; align-items: center; gap: 14px;
    font-size: 16px; color: var(--text-grey);
    height: 30px;
  }
  .contact-list svg { width: 16px; height: 16px; flex: none; }

  .brand-name {
    position: absolute; left: 200px; top: 120px;
    display: flex; align-items: center; gap: 14px;
    font-family: "Audiowide", sans-serif;
    font-size: 58px; letter-spacing: 1px;
    color: var(--white);
  }
  .brand-name .mark-dot {
    width: 22px; height: 22px; border-radius: 50%; background: var(--white);
  }
  .mobile {
    position: absolute; left: 420px; top: 260px;
    display: flex; align-items: center; gap: 10px;
    font-size: 18px; color: var(--white);
  }
  .mobile svg { width: 14px; height: 20px; }
  .holder-name {
    position: absolute; left: 160px; top: 320px;
    font-family: "Audiowide", sans-serif;
    font-size: 18px; letter-spacing: 1.5px;
    color: var(--white);
  }
</style>
</head>
<body>

<section class="card card--front">
  <h1 class="company-name">VELTRANO LDA</h1>
  <p class="address">Rua Almirante Sousa, 42<br>Postal code: 1700-118 Lisboa</p>
  <div class="illustration" role="img" aria-label="Illustration of a blue car and a grey car with a white wrench"></div>
  <ul class="contact-list">
    <li>
      <svg viewBox="0 0 16 16"><path d="M4 1 L7 4 L5 6 Q7 10 10 11 L12 9 L15 12 L13 15 Q4 14 1 3 Z" fill="var(--icon-blue)"/></svg>
      +351 214579326
    </li>
    <li>
      <svg viewBox="0 0 16 16"><rect x="1" y="3" width="14" height="10" fill="var(--icon-blue)"/><path d="M1 3 L8 9 L15 3" fill="none" stroke="var(--card-white)" stroke-width="1.2"/></svg>
      veltrano.oficina@mail.pt
    </li>
    <li>
      <svg viewBox="0 0 16 16"><rect x="1" y="1" width="14" height="14" rx="2" fill="var(--icon-blue)"/></svg>
      veltrano
    </li>
  </ul>
</section>

<section class="card card--back">
  <div class="brand-name"><span class="mark-dot"></span>VELTRANO</div>
  <p class="mobile">
    <svg viewBox="0 0 14 20"><rect x="1" y="1" width="12" height="18" rx="2" fill="none" stroke="var(--white)" stroke-width="1.5"/><line x1="5" y1="16" x2="9" y2="16" stroke="var(--white)" stroke-width="1.5"/></svg>
    +351 913482750
  </p>
  <p class="holder-name">TIAGO MOREIRA</p>
</section>

</body>
</html>
```